Vel-Trax.ch is looking for business card letterhead and envelope C5 with WOW effect

We need a strong business card for our company Vel-Trax.ch, logo is available. You want a black or dark background on which the logo Stark r% 26 # 252; appears. Letterhead and envelope in C5 format should be in a similar design, but does not have to be We need a strong business card for our company Vel-Trax.ch, logo is available. A black or dark background is desired, on which the logo Stark comes across. The letterhead and the envelope in C5 format should have a similar design.

Target Market(s)

Private customers as well as entrepreneurs

Contact Information for Business Card

E-mail: info@vel-trax.ch
Web.www.Vel-Trax.ch
Tel: +41 ( 0 ) 79 684 3027
Adresse:
Lindenhaldeweg 14
9327 Brenzikon

Hier kann man Icons verwenden für Email,Tel und Adressse

Font styles to use
Other font styles liked:
• Dubai,bold

Colors

Designer to choose colors to be used in the design.

Requirements
Must have
• WOW effect
Nice to have
• R% 26 # 252; back business card with our service listings. - VEHICLE LABELING - SHOP WINDOW LABELING - STICKERS AND MUCH MORE ... in red color

```html
<!DOCTYPE html>
<html lang="en">
<head>
<meta charset="utf-8">
<title>Vel-Trax.ch – Stationery</title>
<link rel="stylesheet" href="https://fonts.googleapis.com/css2?family=Quicksand:wght@400;500;700&family=Arimo:wght@400;700&display=swap">
<style>
  :root {
    --backdrop: #e4e4e4;
    --paper: #f0f0f0;
    --ink: #111111;
    --band: #0d0d0d;
    --accent: #f1b80f;
    --grey: #666666;
    --soft-grey: #999999;
    --sans: "Quicksand", sans-serif;
    --body: "Arimo", sans-serif;
  }
  html, body {
    margin: 0;
    width: 1200px;
    height: 2845px;
    overflow: hidden;
    background: var(--backdrop);
  }
  .sheet {
    position: absolute;
    left: 227px;
    width: 745px;
    background: var(--paper);
    overflow: hidden;
  }
  .band {
    position: absolute;
    left: 0; top: 0; bottom: 0;
    width: 58px;
    background: var(--band);
  }
  .band::after {
    content: "";
    position: absolute;
    top: 0; bottom: 0;
    right: -6px;
    width: 4px;
    background: var(--accent);
  }
  .brand {
    position: absolute;
    display: flex;
    align-items: center;
    gap: 14px;
    font-family: var(--sans);
    font-weight: 700;
    color: var(--ink);
    white-space: nowrap;
  }
  .brand-square {
    background: var(--accent);
    flex: none;
  }
  .contact-list {
    position: absolute;
    margin: 0; padding: 0;
    list-style: none;
    font-family: var(--sans);
    color: var(--grey);
    white-space: nowrap;
  }
  .contact-list li {
    display: flex;
    align-items: center;
  }
  .contact-list svg { flex: none; }
  .contact-list .hl { color: var(--accent); font-weight: 700; }
  .address {
    position: absolute;
    margin: 0;
    font-family: var(--sans);
    color: var(--grey);
    font-style: normal;
    white-space: nowrap;
  }

  /* Business card front */
  .card-front { top: 127px; height: 425px; }
  .card-front .brand { left: 154px; top: 80px; font-size: 38px; }
  .card-front .brand-square { width: 22px; height: 22px; }
  .holder {
    position: absolute;
    left: 153px; top: 244px;
    font-family: var(--sans);
  }
  .holder-name {
    margin: 0;
    color: var(--accent);
    font-weight: 700;
    font-size: 24px;
    letter-spacing: 1.5px;
    text-transform: uppercase;
  }
  .holder-role {
    margin: 0;
    color: var(--grey);
    font-size: 21px;
    letter-spacing: 1px;
  }
  .card-front .contact-list { left: 153px; top: 328px; font-size: 21px; line-height: 24px; letter-spacing: .8px; }
  .card-front .contact-list svg { width: 17px; height: 17px; margin-right: 12px; }
  .card-front .address { left: 438px; top: 357px; font-size: 21px; line-height: 25px; letter-spacing: 1.2px; }

  /* Business card back */
  .card-back { top: 632px; height: 425px; background: var(--band); }
  .card-back .texture {
    position: absolute; inset: 0;
    background: linear-gradient(90deg, #101010 0%, #181818 55%, #222222 100%);
  }

  /* Letterhead */
  .letterhead { top: 1162px; height: 942px; }
  .letterhead .band, .envelope .band { width: 44px; }
  .letterhead .brand { left: 135px; top: 78px; font-size: 34px; }
  .letterhead .brand-square, .envelope .brand-square { width: 20px; height: 20px; }
  .letterhead .contact-list { left: 427px; top: 76px; font-size: 13px; line-height: 15.5px; letter-spacing: .4px; }
  .letterhead .contact-list svg,
  .envelope .contact-list svg { width: 11px; height: 11px; margin-right: 8px; }
  .letterhead .address { left: 606px; top: 91px; font-size: 13px; line-height: 15.5px; letter-spacing: .8px; }
  .meta {
    position: absolute;
    top: 268px;
    font-family: var(--body);
    font-size: 14px;
  }
  .meta-label { margin: 0; color: var(--ink); font-weight: 700; }
  .meta-value { margin: 2px 0 0; color: var(--grey); }
  .meta-subject { left: 135px; top: 271px; }
  .meta-date { left: 588px; }
  .letter-body {
    position: absolute;
    left: 135px; top: 378px;
    width: 525px;
    font-family: var(--body);
    color: var(--soft-grey);
  }
  .greeting { margin: 0 0 16px; font-size: 18px; color: var(--grey); }
  .letter-body p.text {
    margin: 0 0 18px;
    font-size: 13.6px;
    line-height: 18px;
    text-align: justify;
  }
  .signature {
    position: absolute;
    left: 135px; top: 811px;
    margin: 0;
    font-family: var(--body);
    font-size: 18px;
    line-height: 22px;
    color: var(--grey);
  }

  /* Envelope C5 */
  .envelope { top: 2182px; height: 527px; }
  .envelope .brand { left: 126px; top: 80px; font-size: 33px; }
  .envelope .contact-list { left: 80px; top: 453px; font-size: 12.5px; line-height: 15px; letter-spacing: .4px; }
  .envelope .address { left: 248px; top: 468px; font-size: 12.5px; line-height: 15px; letter-spacing: .8px; }
</style>
</head>
<body>

<svg width="0" height="0" style="position:absolute">
  <defs>
    <symbol id="icon-phone" viewBox="0 0 20 20">
      <circle cx="10" cy="10" r="10" fill="#f1b80f"/>
      <path d="M6.5 5.5l2 .3.6 2.4-1.2.9a7 7 0 0 0 3 3l.9-1.2 2.4.6.3 2c-4.5.5-8.5-3.5-8-8z" fill="#fff"/>
    </symbol>
    <symbol id="icon-mail" viewBox="0 0 20 20">
      <circle cx="10" cy="10" r="10" fill="#f1b80f"/>
      <rect x="5" y="6.5" width="10" height="7" fill="none" stroke="#fff" stroke-width="1.4"/>
      <path d="M5 6.8l5 4 5-4" fill="none" stroke="#fff" stroke-width="1.4"/>
    </symbol>
    <symbol id="icon-web" viewBox="0 0 20 20">
      <circle cx="10" cy="10" r="10" fill="#f1b80f"/>
      <circle cx="10" cy="10" r="5" fill="none" stroke="#fff" stroke-width="1.4"/>
      <path d="M5 10h10M10 5c-2.5 3-2.5 7 0 10M10 5c2.5 3 2.5 7 0 10" fill="none" stroke="#fff" stroke-width="1.1"/>
    </symbol>
  </defs>
</svg>

<!-- Business card, front -->
<section class="sheet card-front">
  <div class="band"></div>
  <div class="brand"><span class="brand-square"></span>Vel-Trax.ch</div>
  <div class="holder">
    <p class="holder-name">Marco Keller</p>
    <p class="holder-role">Managing Director</p>
  </div>
  <ul class="contact-list">
    <li><svg><use href="#icon-phone"/></svg>+41 ( 0 ) 79 684 3027</li>
    <li><svg><use href="#icon-mail"/></svg>info@vel-trax.ch</li>
    <li><svg><use href="#icon-web"/></svg>www.<span class="hl">Vel-Trax</span>.ch</li>
  </ul>
  <address class="address">Lindenhaldeweg 14<br>9327 Brenzikon</address>
</section>

<!-- Business card, back -->
<section class="sheet card-back">
  <div class="texture" role="img" aria-label="Dark embossed surface with a repeated brand mark pattern"></div>
</section>

<!-- Letterhead -->
<section class="sheet letterhead">
  <div class="band"></div>
  <div class="brand"><span class="brand-square"></span>Vel-Trax.ch</div>
  <ul class="contact-list">
    <li><svg><use href="#icon-phone"/></svg>+41 ( 0 ) 79 684 3027</li>
    <li><svg><use href="#icon-mail"/></svg>info@vel-trax.ch</li>
    <li><svg><use href="#icon-web"/></svg>www.<span class="hl">Vel-Trax</span>.ch</li>
  </ul>
  <address class="address">Lindenhaldeweg 14<br>9327 Brenzikon</address>

  <div class="meta meta-subject">
    <p class="meta-label">SUBJECT :</p>
    <p class="meta-value">Lorem Ipsum is simply dummy</p>
  </div>
  <div class="meta meta-date">
    <p class="meta-label">DATE :</p>
    <p class="meta-value">15-09-2017</p>
  </div>

  <div class="letter-body">
    <p class="greeting">Dear Person,</p>
    <p class="text">Lorem Ipsum is simply dummy text of the printing and typesetting industry. Lorem Ipsum has been the industry's standard dummy text ever since the 1500s, when an unknown printer took a galley of type and scrambled it to make a type specimen book. It has survived not only five centuries, but also the leap into electronic typesetting, remaining essentially unchanged. It was popularised in the 1960s with the release of Dralux sheets containing Lorem Ipsum passages, and more recently with desktop publishing software like Norvel PageSet including versions of Lorem Ipsum.</p>
    <p class="text">Lorem Ipsum is simply dummy text of the printing and typesetting industry. Lorem Ipsum has been the industry's standard dummy text ever since the 1500s, when an unknown printer took a galley of type and scrambled it to make a type specimen book. It has survived not only five centuries, but also the leap into electronic typesetting, remaining essentially unchanged. It was popularised in the 1960s with the release of</p>
    <p class="text">Dralux sheets containing Lorem Ipsum passages, and more recently with desktop publishing software like Norvel PageSet including versions of Lorem Ipsum.lease of Dralux sheets containing Lorem Ipsum passages, and more recently with desktop publishing software like Norvel PageSet including versions of Lorem Ipsum. publishing software like Norvel PageSet including versions of Lorem Ipsum.</p>
  </div>

  <p class="signature">Marco Keller<br>Managing Director</p>
</section>

<!-- Envelope C5 -->
<section class="sheet envelope">
  <div class="band"></div>
  <div class="brand"><span class="brand-square"></span>Vel-Trax.ch</div>
  <ul class="contact-list">
    <li><svg><use href="#icon-phone"/></svg>+41 ( 0 ) 79 684 3027</li>
    <li><svg><use href="#icon-mail"/></svg>info@vel-trax.ch</li>
    <li><svg><use href="#icon-web"/></svg>www.<span class="hl">Vel-Trax</span>.ch</li>
  </ul>
  <address class="address">Lindenhaldeweg 14<br>9327 Brenzikon</address>
</section>

</body>
</html>
```